RFID Blocker - Business Card Design

Design a business card that will be printed onto a plastic RFID blocker wallet card, this card has a space on each side of teh card that will not be printed. One side of the card is to have the contact information, and the other to have a graphic which will symbolize blocking or shielding technology. I like the phrase "Fold Haven". Many people i give this card to may not realize it is a RFID blocker, and i would liek to have small icons on each side representing what it is, see attachment. I will include a few pics found on internet i was using as ideas, and also the RFID card template which shows the area that will not be printed (within the red squares). I like the shield aspect, i was originally thinking of the tarnwick shield with my logo coming out of it like the tarnwick except the black is to dark of a color. the smiley face i use within some of my software. company name is: "vornalux software inc." - I prefer to use small print and no capitals in my company name. company from Canada - my original business card is included in files

Target Market(s)

companies wanting to hire indigenous workers, and indigenous workers looking for employment

Contact Information for Business Card

should include logo with name, title, phone, email and website. our company specializes in first nations indigenous employment software

Font styles to use
Serif
Sans Serif

Requirements
Must have
• Logo
• Name
• Title
• Phone
• email
• website

```html
<!DOCTYPE html>
<html lang="en">
<head>
<meta charset="utf-8">
<title>vornalux software inc. — business card</title>
<link rel="stylesheet" href="https://fonts.googleapis.com/css2?family=Work+Sans:wght@400;500;600&display=swap">
<style>
  :root {
    --stage: #1c1c1d;
    --card: #242425;
    --card-edge: #2b2b2c;
    --brand-blue: #1476d2;
    --logo-grey: #8d9095;
    --text-light: #e9e9ea;
    --badge: #5c5e62;
  }
  * { box-sizing: border-box; margin: 0; padding: 0; }
  html, body {
    width: 1200px; height: 900px; overflow: hidden;
    background: var(--stage);
    font-family: "Work Sans", Arial, sans-serif;
  }
  .stage {
    position: relative; width: 1200px; height: 900px;
    display: flex; flex-direction: column; align-items: center;
    justify-content: center; gap: 40px;
  }
  .card {
    position: relative; width: 620px; height: 354px;
    background: linear-gradient(135deg, var(--card-edge), var(--card) 60%);
    border-bottom: 6px solid var(--brand-blue);
    overflow: hidden;
  }
  .wordmark {
    color: var(--logo-grey);
    font-weight: 500;
    letter-spacing: 1px;
    line-height: 1;
  }
  /* back side */
  .card-back .wordmark {
    position: absolute; left: 196px; top: 120px; font-size: 64px;
  }
  .partner-badge {
    position: absolute; left: 36px; bottom: 22px;
    display: flex; flex-direction: column; align-items: center; gap: 8px;
  }
  .partner-badge__shape {
    width: 44px; height: 44px; border-radius: 50%; background: var(--badge);
  }
  .partner-badge__label {
    color: var(--text-light); font-size: 13px; font-weight: 600;
  }
  /* front side */
  .card-front .wordmark {
    position: absolute; left: 48px; top: 140px; font-size: 56px;
  }
  .divider {
    position: absolute; left: 330px; top: 100px;
    width: 3px; height: 134px; background: var(--brand-blue);
  }
  .contact {
    position: absolute; left: 356px; top: 104px; color: var(--text-light);
  }
  .contact__name {
    color: var(--brand-blue); font-size: 26px; font-weight: 500;
    letter-spacing: 1px; text-transform: uppercase;
  }
  .contact__title { font-size: 18px; margin-bottom: 14px; }
  .contact__list { list-style: none; font-size: 17px; line-height: 1.35; }
  .contact__list li { display: flex; align-items: center; gap: 8px; }
  .contact__list svg { width: 11px; height: 11px; flex: none; }
</style>
</head>
<body>
<main class="stage">
  <section class="card card-back" aria-label="Card back">
    <div class="wordmark">vornalux</div>
    <div class="partner-badge">
      <div class="partner-badge__shape"></div>
      <div class="partner-badge__label">tarnwick Secure</div>
    </div>
  </section>

  <section class="card card-front" aria-label="Card front">
    <div class="wordmark">vornalux</div>
    <div class="divider"></div>
    <div class="contact">
      <h1 class="contact__name">Dean Carrow</h1>
      <p class="contact__title">President</p>
      <ul class="contact__list">
        <li>
          <svg viewBox="0 0 12 12" aria-hidden="true"><path d="M3 1 L5 3.5 L4 5 Q5.5 7 7 8 L8.5 7 L11 9 L10 11 Q4 11 1 3 Z" fill="var(--brand-blue)"/></svg>
          250.555.0142
        </li>
        <li>
          <svg viewBox="0 0 12 12" aria-hidden="true"><rect x="1" y="2.5" width="10" height="7" fill="none" stroke="var(--brand-blue)" stroke-width="1.2"/><path d="M1 2.5 L6 6.5 L11 2.5" fill="none" stroke="var(--brand-blue)" stroke-width="1.2"/></svg>
          dcarrow@vornalux.ca
        </li>
        <li>
          <svg viewBox="0 0 12 12" aria-hidden="true"><circle cx="6" cy="6" r="5" fill="none" stroke="var(--brand-blue)" stroke-width="1.1"/><ellipse cx="6" cy="6" rx="2.2" ry="5" fill="none" stroke="var(--brand-blue)" stroke-width="1"/><path d="M1 6 H11" stroke="var(--brand-blue)" stroke-width="1"/></svg>
          www.vornalux.ca
        </li>
      </ul>
    </div>
  </section>
</main>
</body>
</html>
```